Save the Date card

This will be a Save the Date 5x7 card...preferably Hunter Green background

Annual Fund Leadership Dinner
June 20, 2023. 6:30 pm
Location: The Pellworth's Home
4187 Brimlow Ridge Rd
Harrison, TN 37341

Other side of card:
We would prayerfully ask that you consider partnering with us as we kick off our Annual Fund this Fall to celebrate our 25 year anniversary as an Academy.
Please direct any questions to Marlene Tobbitt, our Director of Advancement 423-555-0176 x 3051 or advancement@fernwickca.org

```html
<!DOCTYPE html>
<html lang="en">
<head>
<meta charset="utf-8">
<title>Annual Fund Leadership Dinner – Save the Date</title>
<link href="https://fonts.googleapis.com/css2?family=Montserrat:wght@500;600;700;800&display=swap" rel="stylesheet">
<style>
  :root {
    --hunter: #234a2b;
    --hunter-deep: #1e3f25;
    --gold: #b9a561;
    --gold-light: #d6bf5a;
    --gold-soft: #a8996a;
    --ink: #2b2b24;
    --white: #ffffff;
    --backdrop: #ececec;
  }
  * { box-sizing: border-box; margin: 0; padding: 0; }
  html, body { width: 1085px; height: 1200px; overflow: hidden; }
  body {
    background: var(--backdrop);
    font-family: "Montserrat", sans-serif;
    position: relative;
  }
  .card {
    position: absolute;
    left: 176px;
    width: 734px;
    height: 525px;
    background: var(--white);
    overflow: hidden;
  }
  .card--front { top: 52px; }
  .card--back { top: 624px; }
  .card-art { position: absolute; inset: 0; width: 734px; height: 525px; }
  .abs { position: absolute; white-space: nowrap; }

  /* front */
  .event-title {
    left: 24px; top: 48px;
    font-weight: 700; font-size: 42px; line-height: 50px;
    letter-spacing: -1px; color: var(--white);
  }
  .event-title .accent { color: var(--gold); }
  .date-icon { left: 20px; top: 250px; }
  .event-date { left: 58px; top: 242px; font-size: 28px; font-weight: 600; color: var(--gold); }
  .date-rule { left: 60px; top: 281px; width: 188px; height: 2px; background: var(--white); }
  .event-time { left: 62px; top: 286px; font-size: 28px; font-weight: 800; color: var(--white); }
  .pin-icon { left: 27px; top: 432px; }
  .venue-name { left: 72px; top: 435px; font-size: 20px; font-weight: 800; color: var(--white); }
  .venue-address { left: 72px; top: 462px; font-size: 17px; font-weight: 500; color: var(--ink); }

  .brand {
    display: flex; flex-direction: column; align-items: center; gap: 6px;
  }
  .brand-dot { width: 58px; height: 58px; border-radius: 50%; background: var(--hunter); }
  .brand-name { font-size: 16px; font-weight: 700; color: var(--hunter); }
  .card--front .brand { left: 612px; top: 392px; }
  .card--back .brand { left: 601px; top: 54px; }

  /* back */
  .appeal {
    left: 24px; top: 34px;
    font-size: 17px; font-weight: 500; line-height: 24.2px; color: var(--white);
  }
  .years-number {
    left: 28px; top: 150px;
    font-size: 78px; font-weight: 800; letter-spacing: -8px; line-height: 1;
    background: linear-gradient(90deg, var(--gold) 0%, var(--gold) 45%, var(--white) 55%);
    -webkit-background-clip: text; background-clip: text; color: transparent;
  }
  .years-label { left: 36px; top: 226px; font-size: 22px; font-weight: 700; color: var(--gold); }
  .anniversary { left: 125px; top: 178px; font-size: 23px; font-weight: 700; color: var(--gold); }
  .anniversary-note { left: 123px; top: 213px; font-size: 17px; font-weight: 500; color: var(--white); }

  .contact-frame-top { left: 31px; top: 282px; width: 34px; height: 2px; background: var(--white); }
  .contact-frame-left { left: 31px; top: 282px; width: 2px; height: 34px; background: var(--white); }
  .contact-frame-right { left: 327px; top: 332px; width: 2px; height: 32px; background: var(--white); }
  .contact-frame-bottom { left: 295px; top: 362px; width: 34px; height: 2px; background: var(--white); }
  .contact-lead { left: 44px; top: 287px; font-size: 17px; font-weight: 500; color: var(--white); }
  .contact-name { left: 44px; top: 312px; font-size: 20px; font-weight: 800; color: var(--hunter); }
  .contact-role { left: 44px; top: 340px; font-size: 17px; font-weight: 500; color: var(--white); }

  .phone-icon { left: 22px; top: 389px; }
  .contact-phone { left: 43px; top: 388px; font-size: 18px; font-weight: 700; color: var(--white); }
  .mail-icon { left: 21px; top: 425px; }
  .contact-email { left: 42px; top: 419px; font-size: 17px; font-weight: 600; color: var(--white); }
  .contact-email .domain { color: var(--gold); }
  .footer-rule { left: 22px; top: 452px; width: 290px; height: 1px; background: rgba(255,255,255,0.7); }
  .social-label { left: 20px; top: 462px; font-size: 10px; font-weight: 600; color: var(--white); }
  .social-list { left: 20px; top: 478px; display: flex; gap: 9px; }
  .social-dot { width: 25px; height: 25px; border-radius: 50%; background: var(--gold-soft); }
</style>
</head>
<body>

<section class="card card--front" aria-label="Save the date, front">
  <svg class="card-art" viewBox="0 0 734 525" aria-hidden="false">
    <defs>
      <linearGradient id="photoDinner" x1="0" y1="0" x2="1" y2="1">
        <stop offset="0" stop-color="#9b8f7c"/>
        <stop offset="0.5" stop-color="#c7c3bb"/>
        <stop offset="1" stop-color="#7f8ea8"/>
      </linearGradient>
      <linearGradient id="goldBandFront" x1="0" y1="0" x2="1" y2="0">
        <stop offset="0" stop-color="#b0a26a"/>
        <stop offset="1" stop-color="#d6bf5a"/>
      </linearGradient>
      <linearGradient id="hunterFade" x1="0" y1="0" x2="1" y2="1">
        <stop offset="0" stop-color="#1e3f25"/>
        <stop offset="1" stop-color="#2a5332"/>
      </linearGradient>
    </defs>
    <g role="img" aria-label="Photo of guests serving themselves from a catered buffet">
      <rect x="0" y="0" width="734" height="404" fill="url(#photoDinner)"/>
    </g>
    <polygon points="0,0 280,0 374,180 172,404 0,404" fill="url(#hunterFade)"/>
    <rect x="0" y="404" width="734" height="112" fill="url(#goldBandFront)"/>
    <polygon points="679,307 734,362 734,525 430,525" fill="#ffffff"/>
    <polygon points="0,515 430,515 422,525 0,525" fill="#234a2b"/>
    <polygon points="430,515 734,515 734,525 422,525" fill="#b9a561"/>
  </svg>

  <h1 class="abs event-title">Annual Fund<br><span class="accent">Leadership</span><br>Dinner</h1>

  <svg class="abs date-icon" width="26" height="26" viewBox="0 0 26 26" fill="none" stroke="#fff" stroke-width="1.6" aria-hidden="true">
    <rect x="2" y="4" width="19" height="18" rx="2"/>
    <line x1="2" y1="9" x2="21" y2="9"/>
    <line x1="7" y1="2" x2="7" y2="6"/><line x1="16" y1="2" x2="16" y2="6"/>
    <circle cx="19" cy="19" r="5" fill="#234a2b"/>
    <polyline points="19,17 19,19 21,20"/>
  </svg>
  <p class="abs event-date">June 20, 2023</p>
  <div class="abs date-rule"></div>
  <p class="abs event-time">6:30 pm</p>

  <svg class="abs pin-icon" width="26" height="34" viewBox="0 0 26 34" aria-hidden="true">
    <path d="M13 1C6.4 1 1 6.2 1 12.8 1 21 13 33 13 33s12-12 12-20.2C25 6.2 19.6 1 13 1z" fill="#2b2b24"/>
    <circle cx="13" cy="12.5" r="4.5" fill="#b9a561"/>
  </svg>
  <p class="abs venue-name">The Pellworth's Home</p>
  <p class="abs venue-address">4187 Brimlow Ridge Rd Harrison, TN 37341</p>

  <div class="abs brand"><span class="brand-dot"></span><span class="brand-name">Fernwick</span></div>
</section>

<section class="card card--back" aria-label="Save the date, back">
  <svg class="card-art" viewBox="0 0 734 525">
    <defs>
      <linearGradient id="photoTable" x1="0" y1="0" x2="1" y2="1">
        <stop offset="0" stop-color="#7a5236"/>
        <stop offset="0.5" stop-color="#c8b9a6"/>
        <stop offset="1" stop-color="#a97a52"/>
      </linearGradient>
      <linearGradient id="goldBandBack" x1="0" y1="0" x2="1" y2="0">
        <stop offset="0" stop-color="#a8996a"/>
        <stop offset="1" stop-color="#d6bf5a"/>
      </linearGradient>
      <linearGradient id="hunterFadeBack" x1="0" y1="0" x2="1" y2="1">
        <stop offset="0" stop-color="#1e3f25"/>
        <stop offset="1" stop-color="#2a5332"/>
      </linearGradient>
    </defs>
    <g role="img" aria-label="Photo of wine glasses set on a restaurant table">
      <polygon points="252,0 610,0 405,275 330,275" fill="url(#photoTable)"/>
    </g>
    <polygon points="0,0 252,0 405,275 0,275" fill="url(#hunterFadeBack)"/>
    <polygon points="0,275 456,275 385,372 0,372" fill="url(#goldBandBack)"/>
    <polygon points="0,372 385,372 283,525 0,525" fill="url(#hunterFadeBack)"/>
  </svg>

  <p class="abs appeal">We would prayerfully ask<br>that you consider<br>partnering with us as we<br>kick off our Annual Fund<br>this Fall to celebrate our</p>
  <p class="abs years-number">25</p>
  <p class="abs years-label">Year</p>
  <p class="abs anniversary">Anniversary</p>
  <p class="abs anniversary-note">as an Academy.</p>

  <div class="abs contact-frame-top"></div>
  <div class="abs contact-frame-left"></div>
  <div class="abs contact-frame-right"></div>
  <div class="abs contact-frame-bottom"></div>
  <p class="abs contact-lead">Please direct any questions to</p>
  <p class="abs contact-name">MARLENE TOBBITT</p>
  <p class="abs contact-role">our Director of Advancement</p>

  <svg class="abs phone-icon" width="14" height="16" viewBox="0 0 14 16" aria-hidden="true">
    <path d="M3 1l3 3-2 2c1 2 3 4 5 5l2-2 3 3-2 3C6 15 0 9 1 3z" fill="#b9a561"/>
  </svg>
  <p class="abs contact-phone">423-555-0176 x 3051</p>
  <svg class="abs mail-icon" width="14" height="10" viewBox="0 0 14 10" aria-hidden="true">
    <rect x="0.5" y="0.5" width="13" height="9" fill="#b9a561"/>
    <polyline points="0.5,0.5 7,5.5 13.5,0.5" fill="none" stroke="#234a2b" stroke-width="1"/>
  </svg>
  <p class="abs contact-email">advancement@<span class="domain">fernwickca</span>.org</p>
  <div class="abs footer-rule"></div>
  <p class="abs social-label">FOLLOW US ON SOCIAL-</p>
  <div class="abs social-list" aria-label="Social channels">
    <span class="social-dot"></span><span class="social-dot"></span><span class="social-dot"></span><span class="social-dot"></span><span class="social-dot"></span>
  </div>

  <div class="abs brand"><span class="brand-dot"></span><span class="brand-name">Fernwick</span></div>
</section>

</body>
</html>
```